Velvet Hounds Website - Boutique online pet store for both owners, their homes and their dogs

I need a high end online store for the sale of dog products (collars, leashes, coats etc), products for their owners (pyjamas, cosmetic bags, pencil cases, gift wrapping paper, greeting cards etc) and the owners home (ring holders, cushion covers, throws etc).

Please peruse the following website for a vauge idea of slightly similar stores:

Mybeaglecorner.example.com.au
Pawtrailhub.example.com.au
Terriertreats.example.com.au
Tallpup.example.co.za

Please keep in mind these are breed specific sites. I intend for the business to sell to trending dog breeds, for example, currently in Australia, French Bulldogs and Dachshunds are trending; therefore this will be the business's current focus.

I also intend for this website to be more elegant and refined than the websites mentioned above. Similar to top names brands, with a hint of cuteness to appeal to the animal lover within customers.

Target Market(s)

Velvet Hounds' target market is majority females, late 20's - 40's, either single, in a relationship, or with children who have left the home. They own small and pampered dogs and treat these dogs like their children. They will have a high disposable income.

I want the brand to attract elitist clientele. Comment has been made that people mightn't be able to spell Velvet when searching for the website; those are not the type of customers I want to attract. I think it may be difficult to encapsulate these two target ideas into the brand; I'd like is to appeal to both the 'Melbourne Socialite' and the Noosa stereotype of "I'm too cool to show it, but I really care what you think"

The products will be, for the most part, unique to the market, a few examples include:

custom hand made collars and leads reflecting current human fashion trends;
leather coats for dogs;
flannel pyjamas for dog;
chef's hats for dogs;
furniture which incorporates dogs beds (blanket box, coffee table, bedside table)
bags, cushions, throw rugs, pyjamas made from various dog print fabrics;
fine leather handbags and purses with various and discreet dog themed embellishments;
custom gift wrapping paper etc etc

Amazing customer service and high quality are two of the core values of Velvet Hounds.

The business will be run through the website as well as high-end markets around Brisbane, Gold Coast and Sunshine Coast.

Colors
eea4c8
ffffff
e34197

Requirements
Must have
• MUST BE FULLY OPERATIONAL ON COMPLETION. I own the domain name www.velvethounds.example.com.au. Needs to be functioning on this domain with an operational online store using Coinvale.
• Must also be mobile friendly.
• Pages:
• For your pup (shopping page)
• For your home (shopping page)
• For you (shopping page)
• Stationery
• Contact us
• I am open to better and more creative page names.
• MUST have an easy to operate back end that I can use to update products as and when required.

```html
<!DOCTYPE html>
<html lang="en">
<head>
<meta charset="utf-8">
<title>Velvet Hounds</title>
<link rel="stylesheet" href="https://fonts.googleapis.com/css2?family=Roboto:wght@300;400;500;700&family=Oswald:wght@400;500&display=swap">
<style>
:root{
  --pink:#e34197;
  --pink-soft:#eea4c8;
  --white:#ffffff;
  --ink:#333333;
  --line:#dddddd;
  --teal:#163e48;
}
*{box-sizing:border-box;margin:0;padding:0}
html,body{width:1200px;height:2804px;overflow:hidden;background:var(--white)}
body{position:relative;font-family:'Roboto',sans-serif;color:var(--ink)}
.abs{position:absolute}

/* header */
.logo{left:97px;top:40px;display:flex;align-items:center;gap:10px}
.logo-square{width:34px;height:34px;background:var(--pink)}
.logo-name{font-weight:700;font-size:22px;color:var(--pink);letter-spacing:.5px}
.cart{left:664px;top:46px;display:flex;gap:14px}
.cart-icon{position:relative;width:44px;height:40px}
.cart-count{position:absolute;left:22px;top:20px;width:24px;height:24px;border-radius:50%;background:var(--pink);color:#fff;font-size:12px;display:flex;align-items:center;justify-content:center}
.cart-text{font-size:14px;color:#555;line-height:19px;padding-top:2px}
.search{left:864px;top:49px;width:237px;height:39px;border:1px solid var(--line);display:flex;align-items:center;justify-content:space-between;padding:0 14px;font-size:11px;color:#777}

/* nav */
.nav{left:0;top:138px;width:1200px;height:51px;background:var(--pink)}
.nav a{position:absolute;top:0;line-height:51px;color:#fff;text-decoration:none;font-size:14px;font-weight:500;letter-spacing:.3px}
.nav .sep{position:absolute;top:0;width:1px;height:51px;background:rgba(255,255,255,.25)}

/* hero */
.hero{left:0;top:189px;width:1200px;height:484px;background:linear-gradient(135deg,#5f7d3c 0%,#9bb56a 35%,#d6d7cc 60%,#b9b8ac 100%)}
.hero-card{left:108px;top:394px;width:391px;height:135px;background:rgba(227,65,151,.92);padding:22px 24px;color:#fff}
.hero-card h1{font-size:34px;font-weight:500;letter-spacing:.3px;line-height:38px}
.hero-card p{font-size:15px;line-height:22px;margin-top:8px}
.hero-arrow{top:430px;width:30px;height:30px;border-radius:50%;background:rgba(255,255,255,.35);display:flex;align-items:center;justify-content:center}

/* welcome */
.section-title{left:0;width:1200px;text-align:center;font-size:32px;font-weight:400;color:#444}
.section-title em{font-style:normal;color:var(--pink)}
.divider{left:500px;width:200px;height:14px}
.welcome-text{left:215px;top:800px;width:770px;text-align:center;font-size:11.5px;line-height:21px;color:#666}
.feature{top:898px;width:300px;text-align:center}
.feature .photo{width:138px;height:138px;margin:0 auto;border-radius:50%;border:3px solid var(--pink-soft)}
.feature h3{margin-top:26px;font-size:18px;font-weight:400;color:#555}
.feature p{margin-top:14px;font-size:11px;line-height:20px;color:#777}

/* featured */
.featured{left:0;top:1198px;width:1200px;height:484px;background:linear-gradient(180deg,#ef8fc4 0%,#e669ad 50%,#e3459a 100%)}
.product{top:1359px;width:314px;height:217px;border:2px solid #fff}
.product .shade{position:absolute;inset:0;background:linear-gradient(90deg,rgba(0,0,0,.35),rgba(0,0,0,0) 70%)}
.product h4{position:absolute;left:20px;top:58px;font-family:'Oswald',sans-serif;font-weight:400;font-size:28px;color:#fff;letter-spacing:-.3px}
.product small{position:absolute;left:22px;top:97px;font-family:'Oswald',sans-serif;font-size:14px;color:#fff;letter-spacing:.3px}
.product .shop{position:absolute;left:20px;top:120px;width:102px;height:30px;background:var(--pink-soft);color:#fff;font-size:11px;text-align:center;line-height:30px}

/* news */
.news-title{left:99px;top:1749px;font-size:22px;font-weight:400;color:#333}
.news-rule{left:342px;top:1762px;width:700px;height:1px;background:#e5e5e5}
.news-arrow{top:1750px;width:24px;height:24px;border-radius:50%;border:1px solid #999}
.post{top:1811px;width:310px}
.post .photo{position:relative;height:191px}
.post .date{position:absolute;left:0;top:0;width:47px;height:58px;background:var(--pink);color:#fff;font-size:14px;line-height:18px;padding:10px 0 0 10px}
.post h5{margin-top:20px;font-size:16px;font-weight:400;color:#333}
.post p{margin-top:12px;font-size:11px;line-height:18px;color:#666}
.post a{display:inline-block;margin-top:12px;font-size:13px;color:#333;text-decoration:underline}

/* photostream */
.gallery-label{left:99px;top:2218px;font-size:19px;color:#333;display:flex;align-items:center;gap:8px}
.gallery{left:99px;top:2256px;width:479px;height:176px;display:grid;grid-template-columns:repeat(4,1fr);grid-template-rows:repeat(2,1fr);gap:3px}
.promo{left:622px;top:2219px;width:479px;height:214px}
.promo-offer{position:absolute;left:0;top:0;width:251px;height:214px;background:var(--pink);color:#fff;text-align:center}
.promo-offer .frame{position:absolute;inset:7px;border:1px dashed rgba(255,255,255,.8)}
.promo-offer .a{position:absolute;top:18px;width:100%;font-family:'Oswald',sans-serif;font-size:32px}
.promo-offer .num{position:absolute;left:70px;top:66px;font-family:'Oswald',sans-serif;font-size:66px;line-height:66px}
.promo-offer .ex{position:absolute;left:148px;top:78px;font-family:'Oswald',sans-serif;font-size:16px}
.promo-offer .pc{position:absolute;left:146px;top:96px;font-family:'Oswald',sans-serif;font-size:34px}
.promo-offer .note{position:absolute;top:154px;width:100%;font-size:9px;letter-spacing:.3px}
.promo-offer .buy{position:absolute;top:172px;width:100%;font-family:'Oswald',sans-serif;font-size:25px}
.promo-side{position:absolute;left:251px;top:0;width:228px;height:214px;background:linear-gradient(135deg,#3a2f2b,#1e1816);display:flex;align-items:center;justify-content:center}
.promo-side span{font-size:14px;font-weight:700;color:#fff;letter-spacing:.5px}

/* footer */
.footer{left:0;top:2468px;width:1200px;height:283px;background:var(--teal)}
.f-text{color:#fff}
.f-brand{left:99px;top:2540px;font-size:21px;font-weight:400}
.f-sub{left:99px;top:2584px;font-size:14px}
.f-input{left:99px;width:254px;height:40px;border:1px solid rgba(255,255,255,.3);font-size:11px;color:#ccc;padding:0 14px;line-height:38px}
.f-btn{left:277px;top:2669px;width:76px;height:40px;background:var(--pink);color:#fff;font-size:12px;text-align:center;line-height:40px}
.f-head{top:2536px;font-size:14px;letter-spacing:.3px}
.f-links{left:463px;top:2574px;font-size:11px;line-height:25px}
.f-social{left:669px;top:2572px;font-size:13px}
.f-social div{display:flex;align-items:center;gap:10px;height:36px}
.f-social i{width:26px;height:26px;border-radius:50%;border:1.5px solid #fff;display:inline-block}
.f-contact{left:858px;top:2566px;font-size:12px;line-height:20px}
.f-row{display:flex;align-items:center;gap:12px;margin-top:12px}
.f-pay{left:858px;top:2676px;font-size:20px;font-weight:700}
.bottom{left:0;top:2751px;width:1200px;height:53px;background:var(--pink);color:#fff;font-size:11px;text-align:center;line-height:53px}
</style>
</head>
<body>

<div class="abs logo"><span class="logo-square"></span><span class="logo-name">VELVET HOUNDS</span></div>
<div class="abs cart">
  <div class="cart-icon">
    <svg width="34" height="34" viewBox="0 0 34 34"><path d="M6 12h22l-2 18H8z" fill="#999"/><path d="M12 12V8a5 5 0 0 1 10 0v4" fill="none" stroke="#999" stroke-width="2"/></svg>
    <span class="cart-count">0</span>
  </div>
  <div class="cart-text">MY CART<br>0 ITEM(S) - $0.00</div>
</div>
<div class="abs search"><span>Search Here</span>
  <svg width="13" height="13" viewBox="0 0 13 13"><circle cx="5.5" cy="5.5" r="4.2" fill="none" stroke="#333" stroke-width="1.8"/><path d="M8.6 8.6L12 12" stroke="#333" stroke-width="2"/></svg></div>

<nav class="abs nav">
  <a style="left:99px">HOME</a><span class="sep" style="left:160px"></span>
  <a style="left:191px">FOR YOUR PUP</a><span class="sep" style="left:316px"></span>
  <a style="left:346px">FOR YOUR HOME</a><span class="sep" style="left:490px"></span>
  <a style="left:514px">FOR YOU</a><span class="sep" style="left:596px"></span>
  <a style="left:626px">PRODUCTS</a><span class="sep" style="left:726px"></span>
  <a style="left:755px">STATIONERY</a><span class="sep" style="left:866px"></span>
  <a style="left:893px">CONTACT US</a>
</nav>

<div class="abs hero" role="img" aria-label="Woman with shopping bags walking a small terrier on a leash along a tree-lined path"></div>
<div class="abs hero-card"><h1>VELVET HOUNDS</h1><p>Lorem ipsum dolor sit amet, consectetur adipisc sed do eiusmod tempor incididunt ut</p></div>
<div class="abs hero-arrow" style="left:44px"><svg width="10" height="14"><path d="M8 1L2 7l6 6" fill="none" stroke="#fff" stroke-width="2"/></svg></div>
<div class="abs hero-arrow" style="left:1126px"><svg width="10" height="14"><path d="M2 1l6 6-6 6" fill="none" stroke="#fff" stroke-width="2"/></svg></div>

<h2 class="abs section-title" style="top:726px">WELCOME TO <em>VELVET HOUNDS</em></h2>
<svg class="abs divider" style="top:772px" viewBox="0 0 200 14"><path d="M10 7h80M110 7h80" stroke="#e7c3d6" stroke-width="1"/><circle cx="100" cy="7" r="3.5" fill="#e34197"/></svg>
<p class="abs welcome-text">Vestibulum commodo volutpat a, convallis ac, laoreet enim. Phasellus fermentum in, dolor pellentesque. Mulla imperdiet sit amet magna. Vestibulum dapibus, Vestibulum commodo volutpat a, convallis ac, laoreet enim. Phasellus fermentum in, dolor pellentesque. Mulla imperdiet sit amet magna. Vestibulum dapibus, Vestibulum commodo volutpat a, convallis ac, laoreet enim. Phasellus fermentum in.</p>

<div class="abs feature" style="left:110px"><div class="photo" role="img" aria-label="Puppy resting on a wrapped gift" style="background:linear-gradient(135deg,#e9d8c6,#c98f63)"></div><h3>GIFTS</h3><p>Sed ut perspiciatis unde omnis iste natus error sit voluptatem accusantium doloremque laudantium, totam rem aperiam, eaque ipsa</p></div>
<div class="abs feature" style="left:448px"><div class="photo" role="img" aria-label="Small fluffy dog with a tape measure" style="background:linear-gradient(135deg,#f2f2f2,#b9b9b9)"></div><h3>HOW TO MEASURE</h3><p>Sed ut perspiciatis unde omnis iste natus error sit voluptatem accusantium doloremque laudantium, totam rem aperiam, eaque ipsa</p></div>
<div class="abs feature" style="left:788px"><div class="photo" role="img" aria-label="Small dog on a leash" style="background:linear-gradient(135deg,#f5f5f5,#8a7a6c)"></div><h3>SIGNS &amp; PRINTS</h3><p>Sed ut perspiciatis unde omnis iste natus error sit voluptatem accusantium doloremque laudantium, totam rem aperiam, eaque ipsa</p></div>

<div class="abs featured"></div>
<h2 class="abs section-title" style="top:1262px;color:#fff">FEATURED PRODUCTS</h2>
<svg class="abs divider" style="top:1306px" viewBox="0 0 200 14"><path d="M10 7h80M110 7h80" stroke="rgba(255,255,255,.6)" stroke-width="1"/><circle cx="100" cy="7" r="3.5" fill="#fff"/></svg>

<div class="abs product" style="left:99px;background:linear-gradient(135deg,#6d7760,#2e2a25)" role="img" aria-label="Dog wearing a leather coat"><div class="shade"></div><h4>LEATHER COATS</h4><small>FORDOGS</small><span class="shop">SHOP NOW!</span></div>
<div class="abs product" style="left:443px;background:linear-gradient(135deg,#6a6c72,#22345a)" role="img" aria-label="Bulldog in flannel pyjamas"><div class="shade"></div><h4>FLANNEL PYJAMAS</h4><small>FORDOGS</small><span class="shop">SHOP NOW!</span></div>
<div class="abs product" style="left:787px;background:linear-gradient(135deg,#5a3f2c,#c9b9a8)" role="img" aria-label="White dog wearing a chef's hat"><div class="shade"></div><h4>CHEF'S HATS</h4><small>FORDOGS</small><span class="shop">SHOP NOW!</span></div>

<h2 class="abs news-title">NEWS AND UPDATES</h2>
<div class="abs news-rule"></div>
<div class="abs news-arrow" style="left:1048px"><svg width="22" height="22"><path d="M13 6l-5 5 5 5" fill="none" stroke="#888" stroke-width="1.5"/></svg></div>
<div class="abs news-arrow" style="left:1077px"><svg width="22" height="22"><path d="M9 6l5 5-5 5" fill="none" stroke="#888" stroke-width="1.5"/></svg></div>

<article class="abs post" style="left:99px"><div class="photo" role="img" aria-label="Black and white portrait of a short-haired dog" style="background:linear-gradient(135deg,#d8d8d8,#3c3c3c)"><span class="date">02<br>JUN</span></div><h5>The Riverbend Pet Spa Dog Wash..</h5><p>Lorem ipsum dolor sit amet, consectetur adipisicing elit, sed do eiusmod tempor incididunt ut labore et dolore magna aliqua. Ut enim ad minim veniam, quis</p><a>READ MORE</a></article>
<article class="abs post" style="left:445px"><div class="photo" role="img" aria-label="Dog wearing sunglasses on a colourful background" style="background:linear-gradient(135deg,#5a8fd6,#c7a27a 60%,#3b62b0)"><span class="date">02<br>JUN</span></div><h5>The Riverbend Pet Spa Dog Wash..</h5><p>Lorem ipsum dolor sit amet, consectetur adipisicing elit, sed do eiusmod tempor incididunt ut labore et dolore magna aliqua. Ut enim ad minim veniam, quis</p><a>READ MORE</a></article>
<article class="abs post" style="left:791px"><div class="photo" role="img" aria-label="Woman walking a large dog in a park" style="background:linear-gradient(135deg,#2f5a24,#7fa150 60%,#3b4a2a)"><span class="date">02<br>JUN</span></div><h5>The Riverbend Pet Spa Dog Wash..</h5><p>Lorem ipsum dolor sit amet, consectetur adipisicing elit, sed do eiusmod tempor incididunt ut labore et dolore magna aliqua. Ut enim ad minim veniam, quis</p><a>READ MORE</a></article>

<div class="abs gallery-label"><svg width="15" height="15"><rect x="1" y="1" width="13" height="13" rx="1" fill="#333"/></svg>Snapgram</div>
<div class="abs gallery" role="img" aria-label="Grid of eight photos of dogs with their owners">
  <div style="background:linear-gradient(135deg,#d9cbb6,#8e7a62)"></div>
  <div style="background:linear-gradient(135deg,#c88a3e,#6f4a22)"></div>
  <div style="background:linear-gradient(135deg,#a9c7e2,#7a9a5a)"></div>
  <div style="background:linear-gradient(135deg,#f3a64b,#3d2a1c)"></div>
  <div style="background:linear-gradient(135deg,#7e9a64,#d6d2c8)"></div>
  <div style="background:linear-gradient(135deg,#ede6dc,#b78a62)"></div>
  <div style="background:linear-gradient(135deg,#3aa6e0,#e2b23c)"></div>
  <div style="background:linear-gradient(135deg,#f1ede8,#b9a58e)"></div>
</div>

<div class="abs promo">
  <div class="promo-offer"><div class="frame"></div>
    <div class="a">WE OFFER A</div>
    <div class="num">20</div><div class="ex">Extra</div><div class="pc">%</div>
    <div class="note">DISCOUNT WHEN CUSTOMERS</div>
    <div class="buy">BUY 1 DOGS BEDS</div>
  </div>
  <div class="promo-side" role="img" aria-label="Dark leather background"><span>VELVET HOUNDS</span></div>
</div>

<footer class="abs footer"></footer>
<div class="abs f-brand f-text">VELVET HOUNDS</div>
<div class="abs f-sub f-text">SUBSCRIBE TO FOLLOW</div>
<div class="abs f-input" style="top:2622px">Enter Name</div>
<div class="abs f-input" style="top:2669px">Enter Email</div>
<div class="abs f-btn">SIGN UP</div>

<div class="abs f-head f-text" style="left:463px">QUICK LINKS</div>
<div class="abs f-links f-text">Contact<br>For your pup<br>For your home<br>For you<br>Stationery</div>

<div class="abs f-head f-text" style="left:669px">OFFERING</div>
<div class="abs f-social f-text"><div><i></i>Pawbook</div><div><i></i>Chirper</div><div><i></i>Circles+</div></div>

<div class="abs f-head f-text" style="left:858px">CONTACT US</div>
<div class="abs f-contact f-text">
  <div>Velvet Hounds<br>PO Box 4410, Ferncourt NSW 2099</div>
  <div class="f-row"><svg width="16" height="16" viewBox="0 0 16 16"><path d="M3 1l3 3-2 2c1 2 3 4 6 6l2-2 3 3-2 2C7 15 1 9 1 3z" fill="none" stroke="#fff" stroke-width="1.3"/></svg>+61 400 555 019</div>
  <div class="f-row"><svg width="16" height="12" viewBox="0 0 16 12"><rect x=".7" y=".7" width="14.6" height="10.6" fill="none" stroke="#fff" stroke-width="1.3"/><path d="M1 1l7 6 7-6" fill="none" stroke="#fff" stroke-width="1.3"/></svg>info@velvethounds.example.com.au</div>
</div>
<div class="abs f-pay f-text">Coinvale</div>

<div class="abs bottom">©2016 velvet hounds., All Rights Reserved.</div>
</body>
</html>
```